Bright Fern Billboard

We need to build a billboard that promotes our dispensary and showcases our Monday thru Thursday deal of 18% off the entire store for Happy Hour. I have attached the logo we want to use. We dont want to use the same colors from the logo as the main colors of the billboard. We need to add both locations to the artwork "5th and Harlow / Corwin and Tilbury". This board needs to POP and have a WOW factor to catch peoples attention. Here are the details outlined:
-Need Bright Fern logo attached to this on the billboard front and center
-Happy Hour - 18% off ENTIRE STORE from 2p-4:20p -Mon -Thurs
-Locations: 5th and Harlow / Corwin and West of Tilbury

```html
<!DOCTYPE html>
<html lang="en">
<head>
<meta charset="utf-8">
<title>Bright Fern Billboard</title>
<link href="https://fonts.googleapis.com/css2?family=Montserrat:wght@500;700&family=Barlow+Semi+Condensed:wght@500;600;700&family=Barlow:wght@500&display=swap" rel="stylesheet">
<style>
  :root {
    --navy: #1b3a6b;
    --teal: #2fe4d6;
    --coral: #ee6f63;
    --white: #ffffff;
    --page: #eef1f5;
  }
  * { margin: 0; padding: 0; box-sizing: border-box; }
  html, body {
    width: 1200px; height: 743px; overflow: hidden;
    background: var(--page);
  }
  .billboard {
    position: absolute; left: 30px; top: 151px;
    width: 1140px; height: 440px;
    overflow: hidden;
    box-shadow: 0 10px 30px rgba(20, 40, 80, 0.18);
  }
  .billboard-bg { position: absolute; inset: 0; }

  .brand {
    position: absolute; left: 60px; top: 112px;
    display: flex; align-items: center; gap: 28px;
  }
  .brand-mark {
    width: 96px; height: 96px; border-radius: 50%;
    background: var(--coral);
    flex: none;
  }
  .brand-text { display: flex; flex-direction: column; }
  .brand-name {
    font-family: "Montserrat", sans-serif; font-weight: 700;
    font-size: 76px; line-height: 1; color: var(--white);
    letter-spacing: -1px; white-space: nowrap;
  }
  .brand-tagline {
    font-family: "Montserrat", sans-serif; font-weight: 700;
    font-size: 21px; letter-spacing: 3.5px; color: var(--white);
    margin-top: 16px; margin-left: 4px; white-space: nowrap;
  }

  .locations {
    position: absolute; left: 60px; top: 340px;
    display: flex; gap: 36px;
  }
  .location { display: flex; align-items: flex-end; gap: 10px; }
  .location-pin { width: 44px; height: 62px; flex: none; }
  .location-text {
    font-family: "Barlow Semi Condensed", sans-serif; font-weight: 600;
    font-size: 26px; color: var(--white);
    border-top: 2px solid var(--white);
    padding-top: 8px; padding-right: 10px; white-space: nowrap;
    margin-bottom: 8px;
  }

  .happy-hour {
    position: absolute; left: 790px; top: 24px; width: 330px;
    text-align: center;
  }
  .hh-happy {
    font-family: "Barlow Semi Condensed", sans-serif; font-weight: 700;
    font-size: 38px; color: var(--white); line-height: 1;
    text-align: right; padding-right: 20px;
  }
  .hh-hour {
    display: flex; justify-content: center; align-items: center;
    font-family: "Barlow Semi Condensed", sans-serif; font-weight: 700;
    font-size: 118px; line-height: 0.9; color: var(--navy);
  }
  .hh-clock {
    width: 92px; height: 92px; border-radius: 50%;
    background: radial-gradient(circle, #f4f4f4 55%, #2a2a2a 58%, #111 100%);
    margin: 0 4px;
  }
  .hh-discount {
    font-family: "Barlow Semi Condensed", sans-serif; font-weight: 700;
    font-size: 84px; line-height: 1; color: var(--white); margin-top: 18px;
  }
  .hh-scope {
    font-family: "Barlow", sans-serif; font-weight: 500;
    font-size: 19px; color: var(--white); letter-spacing: 0.5px; margin-top: 2px;
  }
  .hh-days {
    font-family: "Barlow Semi Condensed", sans-serif; font-weight: 700;
    font-size: 40px; color: var(--white); line-height: 1.1;
  }
  .hh-time {
    font-family: "Barlow Semi Condensed", sans-serif; font-weight: 600;
    font-size: 30px; color: var(--white); line-height: 1.2;
  }
</style>
</head>
<body>
  <main class="billboard">
    <svg class="billboard-bg" width="1140" height="440" viewBox="0 0 1140 440" aria-hidden="true">
      <rect width="1140" height="440" fill="var(--navy)"/>
      <polygon points="800,0 1140,0 1140,440 660,440" fill="var(--white)"/>
      <polygon points="820,0 1140,0 1140,440 682,440" fill="var(--teal)"/>
    </svg>

    <div class="brand">
      <div class="brand-mark"></div>
      <div class="brand-text">
        <span class="brand-name">Bright Fern</span>
        <span class="brand-tagline">CANNABIS DISPENSARY</span>
      </div>
    </div>

    <div class="locations">
      <div class="location">
        <svg class="location-pin" viewBox="0 0 44 62" aria-hidden="true">
          <path d="M22 2C11 2 3 10 3 21c0 14 19 39 19 39s19-25 19-39C41 10 33 2 22 2z" fill="var(--white)"/>
          <circle cx="22" cy="21" r="13" fill="var(--navy)"/>
          <text x="22" y="29" text-anchor="middle" font-family="Montserrat, sans-serif" font-weight="700" font-size="21" fill="var(--white)">1</text>
        </svg>
        <span class="location-text">5th and Harlow / Corwin</span>
      </div>
      <div class="location">
        <svg class="location-pin" viewBox="0 0 44 62" aria-hidden="true">
          <path d="M22 2C11 2 3 10 3 21c0 14 19 39 19 39s19-25 19-39C41 10 33 2 22 2z" fill="var(--white)"/>
          <circle cx="22" cy="21" r="13" fill="var(--navy)"/>
          <text x="22" y="29" text-anchor="middle" font-family="Montserrat, sans-serif" font-weight="700" font-size="21" fill="var(--white)">2</text>
        </svg>
        <span class="location-text">West of Tilbury</span>
      </div>
    </div>

    <section class="happy-hour">
      <div class="hh-happy">Happy</div>
      <div class="hh-hour">
        <span>H</span>
        <div class="hh-clock" role="img" aria-label="Alarm clock standing in for the letter O"></div>
        <span>UR</span>
      </div>
      <div class="hh-discount">18% off</div>
      <div class="hh-scope">ENTIRE STORE</div>
      <div class="hh-days">Monday - Thursday</div>
      <div class="hh-time">from 2p-4:20p</div>
    </section>
  </main>
</body>
</html>
```